New UI for electricity data tool

We are looking for a new UI for the website http://vantorgrid.net. Reassessing the structure of the website is as important as specific design choices. We have created a uniquely comprehensive set of global electricity generation data and now we are looking for creative solutions for how to make this data accessible. Researching and referencing other similar projects may be a good idea.

Goals:
• The website should clearly communicate the most important general conclusions that can be drawn from the data, including:
◦ The world as a whole is not moving away from fossil fuels for electricity generation
◦ There are substantial differences between regions
▪ Some regions have basically solved the problem – they already generate almost all of their electricity from non-fossil sources
▪ Some regions have greatly improved in terms of decarbonizing their electricity generation.
▪ Some regions have greatly deteriorated, in other words they are using a much higher share of fossil fuels to generate their electricity.
◦ There are substantial differences between energy sources. Regions that have successfully decarbonized their electricity generation have usually done so using hydro and/or nuclear. Other low-carbon energy sources have grown quickly in relative terms in the last few years but are so far contributing little in absolute numbers.
• The website should serve as inspiration for energy policy debates. The goal is to study the impact of existing policies around the world. Energy policy here refers to particular combinations of energy sources – ie how much have the countries invested in each type of electricity generation. The tool should help answer questions such as:
◦ Which countries have done the most in terms of decarbonizing their electricity generation?
◦ Which types of energy polices have lead to the fastest decarbonization processes around the world?
◦ If country A changed its energy policy to be more like country B, what would the likely impact be?

Challenges:
• There is a lot of data – it can be overwhelming to the user. It’s crucial to make the site easy to navigate. The main page should highlight the most important data, and it should also be straightforward to find more detailed data.
• Data availability varies from region to region. The current interface addresses this with the default option “Exclude regions with limited data”. We expect a better approach to dealing with this issue. For some regions and years energy sources are grouped together as for example “other renewables” whereas in other cases more detailed data is available.
• Credibility is crucial. Our data is based on a combination of data from KQ and the Tessary Trust. It must be very clear throughout the site where each data set comes from.

Details:
• The current chart color schemes is loosely based on the carbon emissions from each energy source. This should not necessarily be so. The goal is to on the one hand communicate clearly the amounts of fossil vs non-fossil energy that are generated by each region. At the same time we also want to make it easy to view specific energy sources.

Inspirational websites:
• https://www.grafmelo.org/
• https://trendquarrily.org/

Let's simplify. The main metric to focus on is Brisavolt Index and the extent to which the world and each country has achieved it (eg Iceland 100%, France 88% and so on). I'm considering changing the name of the site to BrisavoltIndex.org. We can use maps, charts and perhaps other tools to communicate this main message. What's the best way of doing this?

```html
<!DOCTYPE html>
<html lang="en">
<head>
<meta charset="utf-8">
<title>Brisavolt Index – Energy Sources</title>
<link href="https://fonts.googleapis.com/css2?family=Nunito+Sans:wght@400;600;700&display=swap" rel="stylesheet">
<style>
:root{
  --bg:#f3f3f5;
  --panel:#ffffff;
  --ink:#222226;
  --muted:#6e6e74;
  --line:#8e8e96;
  --soft-line:#f1f1f3;
  --violet:#6a3fe0;
  --violet-soft:#ddd8fb;
  --green:#1fbe14;
  --green-soft:#dcf8d8;
  --orange:#ef5a14;
  --orange-soft:#fde6d3;
  --red:#e8141e;
  --icon:#9a9aa2;
  --chat:#6146e6;
}
*{box-sizing:border-box;margin:0;padding:0}
html,body{width:1200px;height:675px;overflow:hidden}
body{background:var(--bg);font-family:"Nunito Sans",sans-serif;color:var(--ink);position:relative}
.sidebar{position:absolute;left:35px;top:72px;width:43px;height:571px;background:var(--panel);border-radius:4px}
.nav-icon{position:absolute;left:0;width:43px;display:flex;justify-content:center}
.nav-icon svg{width:16px;height:16px}
.nav-active{position:absolute;left:2px;top:200px;width:77px;height:43px;background:var(--bg);border-radius:22px 0 0 22px}
.main{position:absolute;left:112px;top:0;width:1088px;height:675px;background:var(--panel);border-radius:25px 0 0 0}
.years{position:absolute;top:6px;left:0;width:100%;font-size:16px;letter-spacing:1.5px}
.years span{position:absolute;transform:translateX(-50%)}
.card{position:absolute;left:198px;width:640px;border:1px solid var(--line);border-radius:12px;background:var(--panel)}
.card h2{position:absolute;left:18px;font-weight:400;font-size:20px;letter-spacing:1.2px}
.card .sub{position:absolute;left:18px;font-size:10px;letter-spacing:.6px}
.energy{top:79px;height:374px}
.changes{top:470px;height:230px;border-bottom:none;border-radius:12px 12px 0 0}
.dropdown{position:absolute;left:411px;top:11px;width:187px;height:31px;border:1px solid #9a9aa2;border-radius:2px;font-size:15px;color:var(--muted);padding:5px 0 0 22px;letter-spacing:.6px}
.dropdown svg{position:absolute;right:19px;top:10px;width:16px;height:10px}
.row{position:absolute;left:30px;right:42px;font-size:12.5px;letter-spacing:.9px;height:20px}
.row span{position:absolute;top:0}
.row.head{font-weight:700}
.row.sep{border-bottom:1px solid var(--soft-line);height:32px}
.pct{right:0;text-align:right}
.up{color:var(--green)}
.down{color:var(--red)}
.tri{font-size:9px;margin-left:3px;vertical-align:1px}
.stats{position:absolute;left:924px;top:0;width:276px;height:675px}
.stat{position:absolute;left:0;width:276px;height:225px;background:var(--panel);border-radius:0 0 0 25px;box-shadow:-8px 10px 28px rgba(0,0,0,.06)}
.stat .label{position:absolute;left:65px;top:37px;font-size:14px;letter-spacing:2.2px;color:#555}
.stat .value{position:absolute;left:65px;top:58px;font-size:38px;letter-spacing:4px;color:#444}
.stat .delta{position:absolute;left:65px;top:107px;font-size:15px;letter-spacing:1.2px;color:var(--green)}
.stat .chart{position:absolute;left:65px;top:140px}
.badge{position:absolute;left:861px;width:65px;height:65px;border-radius:50%;display:flex;align-items:center;justify-content:center}
.badge svg{width:16px;height:16px}
.chat{position:absolute;left:1131px;top:587px;width:48px;height:48px;border-radius:50%;background:var(--chat);display:flex;align-items:center;justify-content:center;box-shadow:0 6px 16px rgba(97,70,230,.35)}
</style>
</head>
<body>
<nav class="sidebar" aria-label="Main navigation">
  <div class="nav-active"></div>
  <div class="nav-icon" style="top:85px"><svg viewBox="0 0 16 16" fill="none" stroke="var(--icon)" stroke-width="1"><path d="M8 15s5-5 5-8.5A5 5 0 0 0 3 6.5C3 10 8 15 8 15z"/><circle cx="8" cy="6.5" r="1.5"/></svg></div>
  <div class="nav-icon" style="top:141px"><svg viewBox="0 0 16 16"><path d="M10 1 4 9h4l-2 6 6-8H8z" fill="var(--violet)"/></svg></div>
  <div class="nav-icon" style="top:196px"><svg viewBox="0 0 16 16" fill="none" stroke="var(--icon)" stroke-width="1"><path d="M1 12l4-3 3 2 4-5 3-2"/><circle cx="5" cy="9" r="1"/><circle cx="8" cy="11" r="1"/><circle cx="12" cy="6" r="1"/></svg></div>
  <div class="nav-icon" style="top:251px"><svg viewBox="0 0 16 16" fill="none" stroke="var(--icon)" stroke-width="1"><path d="M3 6l5-5 5 5M5 5v8h6V5M6 11l2 3 2-3"/></svg></div>
  <div class="nav-icon" style="top:305px"><svg viewBox="0 0 16 16" fill="none" stroke="#b8bccc" stroke-width="1"><ellipse cx="5" cy="5" rx="4" ry="1.6"/><path d="M1 5v5c0 1 1.8 1.6 4 1.6M1 7.5c0 1 1.8 1.6 4 1.6"/><ellipse cx="11" cy="10" rx="4" ry="1.6"/><path d="M7 10v2c0 1 1.8 1.6 4 1.6s4-.6 4-1.6v-2"/></svg></div>
  <div class="nav-icon" style="top:507px"><svg viewBox="0 0 16 16" fill="none" stroke="#7e8294" stroke-width="1.2"><path d="M2 6c2-2 5 0 6 3s3 3 5 1M4 10l2-2M6 12l2-2M12 3c1 2 1 4-1 6"/></svg></div>
  <div class="nav-icon" style="top:543px"><svg viewBox="0 0 16 16" fill="none" stroke="var(--icon)" stroke-width="1"><circle cx="8" cy="8" r="2.3"/><path d="M8 1.5v2M8 12.5v2M1.5 8h2M12.5 8h2M3.4 3.4l1.4 1.4M11.2 11.2l1.4 1.4M3.4 12.6l1.4-1.4M11.2 4.8l1.4-1.4"/><circle cx="8" cy="8" r="4.6"/></svg></div>
</nav>

<main class="main">
  <div class="years">
    <span style="left:174px">2013</span><span style="left:277px">2014</span><span style="left:381px">2015</span><span style="left:486px">2016</span><span style="left:591px">2017</span><span style="left:697px">2018</span>
  </div>
</main>

<section class="card energy">
  <h2 style="top:12px">Energy Sources</h2>
  <p class="sub" style="top:50px;color:var(--muted)">Regions Grouped By Their Primary Low-Carbon Power Source</p>
  <div class="dropdown">hydro<svg viewBox="0 0 16 10" fill="none" stroke="#555" stroke-width="1.3"><path d="M1 1l7 7 7-7"/></svg></div>
  <div class="row head" style="top:96px"><span style="left:0">Region</span><span style="left:186px">Reason</span><span class="pct">%</span></div>
  <div class="row sep" style="top:144px"><span style="left:0">Guatemala</span><span style="left:186px">Brisavolt Index</span><span class="pct up">+40<span class="tri">▲</span></span></div>
  <div class="row sep" style="top:207px"><span style="left:0">Cambodia</span><span style="left:186px">Brisavolt Index</span><span class="pct down">-10<span class="tri">▼</span></span></div>
  <div class="row sep" style="top:269px"><span style="left:0">Panama</span><span style="left:186px">Brisavolt Index</span><span class="pct up">+35<span class="tri">▲</span></span></div>
  <div class="row" style="top:332px"><span style="left:0">Paraguay</span><span style="left:186px">Brisavolt Index</span><span class="pct up">+67<span class="tri">▲</span></span></div>
</section>

<section class="card changes">
  <h2 style="top:12px">Changes</h2>
  <p class="sub" style="top:45px">Most Significant Increases And Decreases Of Low-Carbon Power</p>
  <div class="row head" style="top:96px"><span style="left:0">Region</span><span style="left:187px">Low-Carbon Power</span><span style="left:383px">Reason</span><span class="pct">%</span></div>
  <div class="row" style="top:144px"><span style="left:0">Guatemala</span><span style="left:187px">75.12% (2009)</span><span style="left:383px">Nuclear Increase</span><span class="pct up">+40<span class="tri">▲</span></span></div>
</section>

<aside class="stats">
  <div class="stat" style="top:0;z-index:3">
    <div class="label">ENERGY SOURCES</div><div class="value">3,456</div><div class="delta">+2.4</div>
    <svg class="chart" width="150" height="42" viewBox="0 0 150 42" fill="none"><path d="M0 30C10 14 22 12 36 22S58 44 70 38 76 22 92 20s26 6 40-2 14-14 16-16" stroke="var(--violet)" stroke-width="1.3"/></svg>
  </div>
  <div class="stat" style="top:225px;z-index:2">
    <div class="label">CHANGES</div><div class="value">124</div><div class="delta">+2.2</div>
    <svg class="chart" style="top:142px" width="150" height="56" viewBox="0 0 150 56" fill="var(--green)">
      <rect x="4" y="8" width="6" height="48"/><rect x="20" y="18" width="6" height="38"/><rect x="36" y="22" width="6" height="34"/><rect x="52" y="18" width="6" height="38"/><rect x="69" y="8" width="6" height="48"/><rect x="85" y="8" width="6" height="48"/><rect x="101" y="28" width="6" height="28"/><rect x="118" y="0" width="6" height="56"/><rect x="134" y="14" width="6" height="42"/>
    </svg>
  </div>
  <div class="stat" style="top:450px;z-index:1">
    <div class="label">GROWTH</div><div class="value">78.7%</div><div class="delta">+4.2</div>
    <svg class="chart" style="top:120px" width="150" height="70" viewBox="0 0 150 70" fill="none"><path d="M0 58c12-8 26-6 40 0s26 12 38 4 12-2 20-10 10-26 22-30 14-14 20-18" stroke="var(--orange)" stroke-width="1.3"/></svg>
  </div>
</aside>

<div class="badge" style="top:51px;background:var(--violet-soft)"><svg viewBox="0 0 16 16"><path d="M10 1 4 9h4l-2 6 6-8H8z" fill="var(--violet)"/></svg></div>
<div class="badge" style="top:276px;background:var(--green-soft)"><svg viewBox="0 0 16 16"><rect x="2" y="5" width="12" height="10" rx="2" fill="var(--green)"/><path d="M5 6V4a3 3 0 0 1 6 0v2" stroke="var(--green)" stroke-width="1.5" fill="none"/><path d="M5.5 9l2.5 2 2.5-2" stroke="#fff" stroke-width="1.2" fill="none"/></svg></div>
<div class="badge" style="top:501px;background:var(--orange-soft)"><svg viewBox="0 0 16 16" fill="none" stroke="var(--orange)" stroke-width="1.5"><path d="M2 12l4-4 3 2 5-5M10 5h4v4"/></svg></div>

<div class="chat" role="button" aria-label="Open chat"><svg width="17" height="17" viewBox="0 0 16 16"><path d="M8 1.5a6.5 6 0 0 0-5.6 9L1.5 14l3.6-1.2A6.5 6 0 1 0 8 1.5z" fill="#fff"/><circle cx="5.2" cy="7.5" r=".9" fill="var(--chat)"/><circle cx="8" cy="7.5" r=".9" fill="var(--chat)"/><circle cx="10.8" cy="7.5" r=".9" fill="var(--chat)"/></svg></div>
</body>
</html>
```